Business card for Tolvery Anesthesia LLC

This is for a business care for Tolvery Anesthesia LLC. Dr. Lisbeth Tolvery, CRNA, DNAP is the sole provider in the LLC. Business address is 4718 N Brackley Street,
Oakhaven, PA 17342
CRNA stands for certified registered nurse anesthetist
"Keeping you safe and comfortable"
I plan to give this business card to the patients that I provide anesthesia to.
Creative design that ties into Anesthesia. Calm soothing colors.

Target Market(s)

Business card for my patients.

Industry/Entity Type

Medicine

Contact Information for Business Card

Creative, professional, eye catching

Logo Text

Tolvery Anesthesia

Font styles to use
Serif
Script

Colors

Designer to choose colors to be used in the design.

Requirements
Must have
• Tolvery Anesthesia
• Dr. Lisbeth Tolvery, CRNA, DNAP
• tolvery.anesthesia@ quillmail.net
Nice to have
• "Keeping you safe and comfortable"
Should not have
• phone number

```html
<!DOCTYPE html>
<html lang="en">
<head>
<meta charset="utf-8">
<title>Tolvery Anesthesia LLC – Business Card</title>
<link rel="stylesheet" href="https://fonts.googleapis.com/css2?family=Libre+Baskerville:ital,wght@0,400;0,700;1,400&family=Pinyon+Script&display=swap">
<style>
  :root {
    --canvas-bg: #ecebe8;
    --card-white: #ffffff;
    --brand-blue: #0a96dd;
    --brand-blue-deep: #0b86cf;
    --brand-blue-light: #4cc0f0;
    --ink: #1d1d1f;
    --stripe-grey: #8a8c90;
    --serif: "Libre Baskerville", Georgia, serif;
    --script: "Pinyon Script", cursive;
  }
  * { box-sizing: border-box; margin: 0; padding: 0; }
  html, body { width: 1200px; height: 891px; overflow: hidden; }
  body { background: var(--canvas-bg); font-family: var(--serif); }

  .canvas {
    position: relative; width: 1200px; height: 891px;
    display: flex; align-items: center; justify-content: center; gap: 50px;
  }
  .card {
    position: relative; width: 525px; height: 300px; overflow: hidden;
    box-shadow: 0 10px 28px rgba(0,0,0,.18);
  }
  .card-art { position: absolute; inset: 0; }

  /* front */
  .card--front { background: var(--card-white); }
  .brand { position: absolute; display: flex; align-items: center; gap: 10px; }
  .brand-dot { width: 30px; height: 30px; border-radius: 50%; background: var(--brand-blue); flex: none; }
  .brand-name {
    font-family: var(--serif); font-weight: 700; text-transform: uppercase;
    line-height: 1.05; letter-spacing: .5px;
  }
  .card--front .brand { left: 44px; top: 34px; }
  .card--front .brand-name { color: var(--ink); font-size: 19px; }

  .holder { position: absolute; left: 44px; top: 118px; }
  .holder-name { font-size: 17px; font-weight: 700; color: var(--ink); }
  .holder-creds { font-size: 11px; font-style: italic; color: var(--brand-blue); margin-top: 4px; }
  .holder-email {
    display: flex; align-items: center; gap: 6px; margin-top: 12px;
    font-size: 10px; color: var(--ink);
  }
  .holder-email svg { width: 13px; height: 10px; }

  .tagline { position: absolute; font-family: var(--script); color: #fff; line-height: 1.15; }
  .card--front .tagline { right: 36px; bottom: 30px; font-size: 26px; text-align: left; }

  /* back */
  .card--back { background: linear-gradient(160deg, var(--brand-blue-light) 0%, var(--brand-blue) 40%, var(--brand-blue-deep) 100%); }
  .card--back .brand { left: 50%; top: 88px; transform: translateX(-50%); }
  .card--back .brand-dot { background: #fff; }
  .card--back .brand-name { color: #fff; font-size: 18px; }
  .card--back .tagline { left: 0; right: 0; top: 158px; text-align: center; font-size: 30px; }
</style>
</head>
<body>
<main class="canvas">

  <section class="card card--front" aria-label="Business card front">
    <svg class="card-art" viewBox="0 0 525 300" aria-hidden="true">
      <defs>
        <linearGradient id="frontBlue" x1="0" y1="1" x2="1" y2="0">
          <stop offset="0" stop-color="#0b86cf"/>
          <stop offset="1" stop-color="#1fa6e8"/>
        </linearGradient>
        <radialGradient id="frontGlow" cx=".6" cy=".45" r=".5">
          <stop offset="0" stop-color="#6fd0f6" stop-opacity=".8"/>
          <stop offset="1" stop-color="#6fd0f6" stop-opacity="0"/>
        </radialGradient>
      </defs>
      <path d="M150,300 C215,210 320,166 525,134 L525,143 C325,176 227,218 163,300 Z" fill="var(--stripe-grey)"/>
      <path d="M172,300 C232,222 332,184 525,156 L525,300 Z" fill="url(#frontBlue)"/>
      <path d="M330,300 C310,240 350,190 440,175 C420,220 420,260 470,300 Z" fill="url(#frontGlow)"/>
    </svg>

    <div class="brand">
      <span class="brand-dot"></span>
      <span class="brand-name">Tolvery<br>Anesthesia</span>
    </div>

    <div class="holder">
      <p class="holder-name">Dr. Lisbeth Tolvery,</p>
      <p class="holder-creds">CRNA, DNAP</p>
      <p class="holder-email">
        <svg viewBox="0 0 13 10"><rect x=".5" y=".5" width="12" height="9" fill="none" stroke="var(--brand-blue)"/><path d="M.5,.5 L6.5,5.5 L12.5,.5" fill="none" stroke="var(--brand-blue)"/></svg>
        tolvery.anesthesia@ quillmail.net
      </p>
    </div>

    <p class="tagline">Keeping you safe<br>and comfortable...</p>
  </section>

  <section class="card card--back" aria-label="Business card back">
    <svg class="card-art" viewBox="0 0 525 300" aria-hidden="true">
      <path d="M0,0 L525,0 L525,40 C420,10 300,10 200,70 C140,105 60,110 0,95 Z" fill="#ffffff" fill-opacity=".10"/>
      <path d="M0,300 L0,230 C120,270 260,280 380,240 C440,220 490,200 525,195 L525,300 Z" fill="#ffffff" fill-opacity=".12"/>
      <path d="M0,260 C140,290 300,285 525,220" fill="none" stroke="#ffffff" stroke-opacity=".25" stroke-width="1.5"/>
    </svg>

    <div class="brand">
      <span class="brand-dot"></span>
      <span class="brand-name">Tolvery<br>Anesthesia</span>
    </div>

    <p class="tagline">Keeping you safe<br>and comfortable...</p>
  </section>

</main>
</body>
</html>
```